Lumo Cellar Traders needs a new business card design

Colour theme: Gold + Red preferred
Front side: Main logo with my details as below;
Back side: Theme of some wine glasses or bottles, maybe different color of log together
Lumo Cellar Traders

Leo Park
박 성민 (this is Korean character) on the English typying board: qkr tjdals
Managing Director

Suite 7/5 Harlow Rd
Bayfield WA 6923
Tel) +61(8) 6027 3518
Mob) +61(412) 305 276

leo.park@lumocellartraders.example
lumocellar@lumocellartraders.example
www.lumocellartraders.example

Target Market(s)

Asian Market

Industry/Entity Type

Business

Contact Information for Business Card

Lumo Cellar Traders

Leo Park
박 성민 (this is Korean character) English typying: qkr tjdals
Managing Director

Suite 7/5 Harlow Rd
Bayfield WA 6923
Tel) +61(8) 6027 3518
Mob) +61(412) 305 276

Font styles to use
Serif
Decorative

Colors
ec1f27
f78f21
f04a50
faa54b
cadf82
abd036

Requirements
Must have
• Company Logo & wine theme
Nice to have
• Very simple & modern
Should not have
• No Red Color on the name of Leo Park or 박 성민
• No traditional looking. young and modern look preferred

```html
<!DOCTYPE html>
<html lang="en">
<head>
<meta charset="utf-8">
<title>Lumo Cellar Traders – Business Card</title>
<link rel="stylesheet" href="https://fonts.googleapis.com/css2?family=Tinos:wght@400;700&family=Noto+Serif+KR:wght@400&display=swap">
<style>
  :root {
    --bg: #e9e6e2;
    --card: #ffffff;
    --red: #d8242a;
    --red-deep: #b81c22;
    --gold: #c9982f;
    --gold-text: #b8862a;
    --ink: #1b1b1b;
    --faint: #f6ece8;
  }
  * { margin: 0; padding: 0; box-sizing: border-box; }
  html, body { width: 1200px; height: 880px; overflow: hidden; }
  body { background: var(--bg); font-family: "Tinos", "Times New Roman", serif; color: var(--ink); position: relative; }

  .card {
    position: absolute; width: 620px; height: 354px;
    background: var(--card); border-radius: 22px; overflow: hidden;
    box-shadow: 0 6px 18px rgba(0,0,0,.12);
  }
  .card--brand { left: 80px; top: 60px; }
  .card--details { left: 500px; top: 466px; }

  .brand { display: flex; align-items: center; gap: 14px; }
  .brand__dot { width: 46px; height: 46px; border-radius: 50%; background: var(--red); flex: none; }
  .brand__name { font-family: "Tinos", serif; font-weight: 700; color: var(--red); font-size: 34px; line-height: 1; letter-spacing: .5px; }

  .card--brand .brand { position: absolute; left: 50%; top: 128px; transform: translateX(-50%); white-space: nowrap; }
  .website { position: absolute; left: 0; right: 0; top: 212px; text-align: center; font-size: 17px; }
  .website__domain { color: var(--red); }

  .decor { position: absolute; inset: 0; }
  .watermark { position: absolute; left: 330px; top: 30px; width: 220px; height: 220px; border-radius: 50%;
    background: radial-gradient(circle, var(--faint) 0%, rgba(246,236,232,0) 70%); }

  .card--details .brand { position: absolute; left: 44px; top: 48px; }
  .card--details .brand__dot { width: 40px; height: 40px; }
  .card--details .brand__name { font-size: 28px; }

  .person { position: absolute; left: 44px; top: 142px; display: flex; align-items: baseline; gap: 10px; white-space: nowrap; }
  .person__name { color: var(--gold-text); font-weight: 700; font-size: 24px; }
  .person__rule { width: 1px; height: 22px; background: var(--red); align-self: center; }
  .person__local { font-family: "Noto Serif KR", serif; font-size: 17px; }
  .person__latin { font-size: 17px; }

  .contacts { position: absolute; left: 44px; top: 186px; list-style: none; }
  .contacts li { display: flex; align-items: center; gap: 10px; font-size: 16px; height: 26px; }
  .icon { width: 18px; height: 18px; flex: none; }
</style>
</head>
<body>

<section class="card card--brand" aria-label="Card back with company name">
  <div class="brand">
    <span class="brand__dot"></span>
    <span class="brand__name">Lumo Cellar Traders</span>
  </div>
  <p class="website">www.<span class="website__domain">lumocellartraders</span>.example</p>
</section>

<section class="card card--details" aria-label="Card front with contact details">
  <div class="watermark" role="img" aria-label="Faint brand mark area"></div>
  <svg class="decor" viewBox="0 0 620 354" aria-hidden="true">
    <defs>
      <linearGradient id="band-red" x1="0" y1="0" x2="1" y2="1">
        <stop offset="0" stop-color="#e0292f"/>
        <stop offset="1" stop-color="#b81c22"/>
      </linearGradient>
    </defs>
    <path d="M430 0 C515 50 560 200 620 300 L620 0 Z" fill="url(#band-red)"/>
    <path d="M385 0 C490 60 535 215 620 335" fill="none" stroke="#c9982f" stroke-width="9"/>
  </svg>

  <div class="brand">
    <span class="brand__dot"></span>
    <span class="brand__name">Lumo Cellar Traders</span>
  </div>

  <div class="person">
    <span class="person__name">Leo Park</span>
    <span class="person__rule"></span>
    <span class="person__local">박 성민</span>
    <span class="person__latin">qkr tjdals</span>
  </div>

  <ul class="contacts">
    <li>
      <svg class="icon" viewBox="0 0 18 18"><circle cx="9" cy="9" r="8" fill="none" stroke="#d8242a" stroke-width="1.4"/><path d="M5 7 h8 v5 h-8 z M6.5 7 l1-2 h3 l1 2" fill="#d8242a"/></svg>
      +61(8) 6027 3518
    </li>
    <li>
      <svg class="icon" viewBox="0 0 18 18"><circle cx="9" cy="9" r="8" fill="none" stroke="#d8242a" stroke-width="1.4"/><rect x="6.5" y="4" width="5" height="10" rx="1" fill="none" stroke="#d8242a" stroke-width="1.3"/></svg>
      +61(412) 305 276
    </li>
    <li>
      <svg class="icon" viewBox="0 0 18 18"><circle cx="9" cy="9" r="8" fill="none" stroke="#d8242a" stroke-width="1.4"/><rect x="4.5" y="6" width="9" height="6.5" fill="#d8242a"/><path d="M4.5 6 L9 9.5 L13.5 6" fill="none" stroke="#fff" stroke-width="1"/></svg>
      leo.park@lumocellartraders.example
    </li>
    <li>
      <svg class="icon" viewBox="0 0 18 18"><circle cx="9" cy="9" r="8" fill="none" stroke="#d8242a" stroke-width="1.4"/><rect x="4.5" y="6" width="9" height="6.5" fill="#d8242a"/><path d="M4.5 6 L9 9.5 L13.5 6" fill="none" stroke="#fff" stroke-width="1"/></svg>
      lumocellar@lumocellartraders.example
    </li>
    <li>
      <svg class="icon" viewBox="0 0 18 18"><circle cx="9" cy="9" r="8" fill="none" stroke="#d8242a" stroke-width="1.4"/><path d="M9 14 C6 10.5 5.5 9 5.5 7.5 a3.5 3.5 0 0 1 7 0 C12.5 9 12 10.5 9 14 Z" fill="#d8242a"/><circle cx="9" cy="7.5" r="1.3" fill="#fff"/></svg>
      Suite 7/5 Harlow Rd Bayfield WA 6923
    </li>
  </ul>
</section>

</body>
</html>
```